Book Cover

Hello!
I need someone to design a book cover with the title, subtitle and one of the photos attached.

- Title: Beyond the Grey Hours - By Corwin Ashdale
- Subtitle: A Steady Handbook for finding calm and strength after hard news.

```html
<!DOCTYPE html>
<html lang="en">
<head>
<meta charset="utf-8">
<title>Beyond the Grey Hours — Corwin Ashdale</title>
<link rel="stylesheet" href="https://fonts.googleapis.com/css2?family=Bebas+Neue&display=swap">
<style>
  :root {
    --backdrop: #e6e6e6;
    --cover: #f5f5f4;
    --ink-grey: #3f3f3f;
    --ink-blue: #4264a8;
    --photo-sky: #cfe0ee;
    --photo-mid: #8fa4c4;
    --photo-deep: #2f4f9a;
    --photo-warm: #8c7a5e;
  }
  html, body {
    margin: 0;
    padding: 0;
    width: 1200px;
    height: 1000px;
    overflow: hidden;
    background: var(--backdrop);
  }
  .book-cover {
    position: absolute;
    left: 300px;
    top: 50px;
    width: 600px;
    height: 900px;
    background: var(--cover);
    box-shadow: 0 10px 30px rgba(0,0,0,0.12);
    overflow: hidden;
  }
  .cover-photo {
    position: absolute;
    left: 0;
    top: 0;
    width: 600px;
    height: 480px;
  }
  .title-block {
    position: absolute;
    right: 44px;
    top: 500px;
    width: 530px;
    margin: 0;
    text-align: right;
    font-family: "Bebas Neue", "Oswald", sans-serif;
    font-weight: 400;
    line-height: 0.9;
  }
  .title-lead {
    display: block;
    font-size: 62px;
    color: var(--ink-grey);
    letter-spacing: 1px;
  }
  .title-main {
    display: block;
    font-size: 118px;
    color: var(--ink-blue);
    letter-spacing: 1px;
  }
  .subtitle {
    display: block;
    margin-top: 6px;
    font-size: 19px;
    color: var(--ink-blue);
    letter-spacing: 0.4px;
    line-height: 1.1;
    white-space: nowrap;
  }
  .author {
    display: block;
    margin-top: 40px;
    font-size: 58px;
    color: var(--ink-grey);
    letter-spacing: 1px;
  }
</style>
</head>
<body>
  <main class="book-cover">
    <svg class="cover-photo" viewBox="0 0 600 480" role="img" aria-label="Portrait photo of an older bearded man in a blue jacket, looking up outdoors against a pale winter sky, framed by a rough brushed edge">
      <defs>
        <linearGradient id="photo-tone" x1="0" y1="0" x2="0.6" y2="1">
          <stop offset="0" stop-color="var(--photo-sky)"/>
          <stop offset="0.35" stop-color="var(--photo-mid)"/>
          <stop offset="0.55" stop-color="var(--photo-warm)" stop-opacity="0.85"/>
          <stop offset="1" stop-color="var(--photo-deep)"/>
        </linearGradient>
      </defs>
      <path fill="url(#photo-tone)" d="
        M0 200
        L20 184 L28 206 L44 176 L60 194 L72 160 L90 186 L104 148 L118 178 L132 130 L150 164
        L164 112 L180 152 L196 96 L212 136 L226 84 L244 120 L258 70 L276 112 L292 62
        L306 102 L318 56 L334 96 L346 64 L352 112 L360 160 L352 200 L368 236 L360 276
        L372 310 L362 340 L374 362 L358 370 L346 404 L334 384 L322 440 L306 402 L296 460
        L280 418 L268 470 L252 430 L240 466 L226 424 L212 456 L198 416 L184 446 L170 404
        L156 430 L140 392 L120 414 L100 378 L80 400 L60 362 L40 378 L20 350 L0 364 Z"/>
    </svg>

    <h1 class="title-block">
      <span class="title-lead">Beyond the</span>
      <span class="title-main">Grey Hours</span>
      <span class="subtitle">A Steady Handbook for finding calm and strength after hard news.</span>
      <span class="author">Corwin Ashdale</span>
    </h1>
  </main>
</body>
</html>
```